Business Cards for Marco and Tobin

Design of business cards for two people with the recently created brand Valcor Mobile. Valcor Mobile wants to become a worldwide major player on the secondhand phone market. It gathers send hand phones from individuals, refurbish them and sell them throughout the world. It has a green impact (recycling) and we also contribute to social project in Africa (a percentage of our benefits are sent to build school, sport facilities, etc.

Target Market(s)

B2B - Marco and Tobin are in contact with distributors across Africa.

Industry/Entity Type

Wireless Communication

Contact Information for Business Card

Marco Feuillet
Head of Emerging Markets
Valcor Energy South Africa (Pty) Ltd
Kestrel Road 47
2031 Sandton - Johannesburg
South Africa
Tel: + 27 10 555 0148
Mobile : +27 82 55 104
Email : marco.feuillet@valcormobile.example
Skype: marco.feuillet
Web: www.valcormobile.example
 

Tobin Farrow
Head of Southern Africa
Kestrel Road 47
South Africa
Tel: + 27 10 555 0148
Mobile: +27 83 555 0276
Email: tobin.farrow@valcormobile.example
Skype: tobin.farrow
Web: www.valcormobile.example

Requirements
Must have
• The cards need to be "serious", trustable, with a worldwide presence.
Nice to have
• Some "green" / recycling touch would be nice but not necessary if in contradiction with the general design.

```html
<!DOCTYPE html>
<html lang="en">
<head>
<meta charset="utf-8">
<title>Valcor Mobile – Business Card</title>
<link rel="stylesheet" href="https://fonts.googleapis.com/css2?family=Open+Sans:wght@400;600;700&display=swap">
<style>
  :root {
    --backdrop: #a6a6a6;
    --card: #efeeee;
    --green: #25733f;
    --line: #8fbf9c;
    --ink: #333333;
    --ink-soft: #4a4a4a;
    --blue: #2f8fd8;
    --navy: #11304d;
  }
  html, body {
    margin: 0;
    padding: 0;
    width: 1073px;
    height: 1200px;
    overflow: hidden;
    background: var(--backdrop);
    font-family: "Open Sans", Arial, sans-serif;
  }
  .card {
    position: absolute;
    width: 791px;
    height: 457px;
    background: var(--card);
    box-shadow: 2px 3px 5px rgba(0,0,0,0.35);
  }
  .card--front { left: 141px; top: 141px; }
  .card--back  { left: 144px; top: 658px; }
  .card svg { display: block; width: 100%; height: 100%; }
  .accent { fill: var(--green); }
  .rule { stroke: var(--line); stroke-width: 1.6; fill: none; }
  .icon { stroke: #ffffff; stroke-width: 1.8; fill: none; stroke-linecap: round; }
  .name { font-size: 21px; font-weight: 700; fill: var(--ink); }
  .name .surname { fill: var(--blue); }
  .role { font-size: 15.5px; fill: var(--ink-soft); }
  .company { font-size: 19.5px; font-weight: 700; fill: var(--ink); }
  .address { font-size: 16px; fill: var(--ink-soft); }
  .contact { font-size: 16.5px; fill: var(--ink-soft); }
  .web { font-size: 19px; fill: var(--ink-soft); }
  .brand { font-size: 37px; font-weight: 600; fill: var(--navy); letter-spacing: -0.5px; }
  .brand-mark { fill: var(--blue); }
</style>
</head>
<body>

<div class="card card--front">
  <svg viewBox="0 0 791 457" xmlns="http://www.w3.org/2000/svg">
    <polygon class="accent" points="261,0 396,0 328,63"/>
    <polygon class="accent" points="791,291 690,392 754,457 791,457"/>
    <line class="rule" x1="328" y1="63" x2="328" y2="394"/>
    <line class="rule" x1="71" y1="394" x2="692" y2="394"/>

    <polygon class="accent" points="71,368 97,394 71,420 45,394"/>
    <path class="icon" d="M65,386 q-3,3 0,8 q4,7 10,10 q4,2 6,-1 l-4,-4 l-3,2 q-4,-2 -6,-6 l2,-3 z"/>

    <polygon class="accent" points="330,366 356,392 330,418 304,392"/>
    <g class="icon">
      <circle cx="330" cy="392" r="9"/>
      <ellipse cx="330" cy="392" rx="4" ry="9"/>
      <line x1="321" y1="392" x2="339" y2="392"/>
    </g>

    <text class="name" x="192" y="174" text-anchor="middle">MARCO <tspan class="surname">FEUILLET</tspan></text>
    <text class="role" x="192" y="198" text-anchor="middle">Head of Emerging Markets</text>

    <text class="company" x="374" y="168">Valcor Energy South Africa (Pty) Ltd</text>
    <text class="address" x="374" y="191">Kestrel Road 47</text>
    <text class="address" x="374" y="213">2031 Sandton - Johannesburg</text>
    <text class="address" x="374" y="235">South Africa</text>

    <text class="contact" x="109" y="383">+27 82 55 104</text>
    <text class="contact" x="104" y="417">+ 27 10 555 0148</text>

    <text class="contact" x="376" y="385">skype: marco.feuillet</text>
    <text class="contact" x="376" y="414">marco.feuillet@valcormobile.example</text>
  </svg>
</div>

<div class="card card--back">
  <svg viewBox="0 0 790 458" xmlns="http://www.w3.org/2000/svg">
    <polygon class="accent" points="745,0 688,60 790,162 790,0"/>
    <polygon class="accent" points="259,458 396,458 328,391"/>
    <line class="rule" x1="71" y1="60" x2="690" y2="60"/>
    <line class="rule" x1="328" y1="61" x2="328" y2="392"/>

    <polygon class="accent" points="71,32 99,60 71,88 43,60"/>
    <polygon class="accent" points="328,33 356,61 328,89 300,61"/>

    <text class="web" x="434" y="47">www.valcormobile.example</text>

    <rect class="brand-mark" x="521" y="228" width="44" height="44" rx="4"/>
    <text class="brand" x="543" y="331" text-anchor="middle">Valcor Mobile</text>
  </svg>
</div>

</body>
</html>
```